Tidal Bloomz - Sovereign rings, pendants & custom cultural pieces

I need a website that attracts customers knowing that I am as per detailed below Everyone deserves a special piece of treasure. At Tidal Bloomz we provide you with unique, high-quality and affordable Sovereign rings, pendants & custom cultural pieces.
Feel free to check my Picorama page to get idea's @tidal.bloomz
I want people to see the Items I have available & know that my prices are very competitive. I want people to be able to Shop/Purchase items via site. I would like to have Tidal Bloomz Friendlio, Picorama & Swapzo Icon/tabs on site so customers can link a at click of the mouse.

(My Apologies to you all, This is all overwhelming & new to myself & I appreciate your efforts & work detail)
Updates

Apologies, have had family loss to deal with

Still dealing with loss of family member

Still Dealing with Family member passing

As previously, still getting through the loss of a family member

As per previous extensions, re adjusting to life after loss of family member

As per previously still recovering from loss of family member

As previously expressed

Haven’t recovered from family loss

I am still getting life back together

Target Market(s)

Jewellery, Wedding, Gifts, Pacific people, Persons 18 - 65yrs, New Zealand & Australian

Industry/Entity Type

Jewelry

Contact Information for Business Card

Tidal Bloomz
Reko Tumanu
Friendlio @tidalbloomz
Picorama @tidal.bloomz
Phone Number 021 07351942
Website www.tidalbloomz-example.co.nz
Auckland
New Zealand

Number of Pages Required

5+ page

Font styles to use
Sans Serif

Colors
474747
1b1b1b
000000
cfcfcf
fbed22
ffc214
ffffff

Requirements
Must have
• Using Black / Gold Tidal Bloomz logo with crown, has been attached to Web design.
• Reko Tumanu
• Friendlio Tidal Bloomz
• Picorama @tidal.bloomz
• Swapzo Tidal Bloomz
• Phone Number 021 07351942
• Website www.tidalbloomz-example.co.nz
Nice to have
• Thinking black card with the Tidal Bloomz Gold logo
• Lines on back of card for Customer Quoted Prices

```html
<!DOCTYPE html>
<html lang="en">
<head>
<meta charset="utf-8">
<title>Tidal Bloomz — Shop</title>
<link rel="stylesheet" href="https://fonts.googleapis.com/css2?family=Montserrat:wght@400;500&family=Open+Sans:wght@400;600;700&family=Raleway:wght@400&display=swap">
<style>
:root{
  --black:#000000;
  --ink:#1b1b1b;
  --panel:#262626;
  --footer:#121212;
  --grey:#474747;
  --light:#cfcfcf;
  --white:#ffffff;
  --gold:#ffc214;
  --gold-deep:#c9a227;
  --lemon:#fbed22;
}
*{box-sizing:border-box;margin:0;padding:0}
html,body{width:1052px;height:1200px;overflow:hidden;background:var(--ink)}
body{position:relative;font-family:'Montserrat',sans-serif;color:var(--white)}
.abs{position:absolute}

.site-header{position:absolute;left:0;top:0;width:1052px;height:112px;background:var(--ink)}
.nav-link{position:absolute;top:46px;font-size:12px;letter-spacing:1.6px;color:var(--white);text-decoration:none;transform:translateX(-50%)}
.brand{position:absolute;left:526px;top:40px;transform:translateX(-50%);display:flex;align-items:center;gap:8px;color:var(--gold-deep);font-family:'Montserrat',sans-serif;font-weight:500;font-size:15px;letter-spacing:1px;white-space:nowrap}
.brand-mark{width:10px;height:10px;background:var(--gold-deep)}

.filter-bar{position:absolute;left:0;top:112px;width:1052px;height:61px;background:var(--panel)}
.crumbs{position:absolute;left:32px;top:24px;font-size:12.5px;letter-spacing:1.6px}
.chip{position:absolute;top:16px;height:24px;padding:0 7px;background:var(--grey);font-size:11.5px;letter-spacing:1px;line-height:24px;color:var(--white)}
.sort-label{position:absolute;left:801px;top:24px;font-size:11.5px;letter-spacing:1.5px}
.sort-select{position:absolute;left:870px;top:12px;width:100px;height:33px;border:1.5px solid var(--white);font-size:11.5px;letter-spacing:1px;padding:7px 0 0 8px}
.sort-select svg{position:absolute;right:7px;top:13px}

.filters{position:absolute;left:19px;top:207px;width:179px;height:349px;background:var(--panel);font-family:'Open Sans',sans-serif}
.filters h2{position:absolute;left:13px;top:16px;font-family:'Montserrat',sans-serif;font-size:11.5px;font-weight:500;letter-spacing:1.6px}
.filter-row{position:absolute;left:15px;display:flex;align-items:center;gap:14px;font-size:11.5px;color:var(--white)}
.toggle{width:14px;height:14px;border:1px solid var(--white);position:relative}
.toggle::before{content:"";position:absolute;left:2px;right:2px;top:6px;height:1px;background:var(--white)}
.toggle.closed::after{content:"";position:absolute;top:2px;bottom:2px;left:6px;width:1px;background:var(--white)}
.size-opt{position:absolute;left:37px;display:flex;align-items:center;gap:7px;font-size:11.5px}
.box{width:11px;height:11px;border:1px solid var(--white);position:relative}
.box.on::after{content:"";position:absolute;left:2px;top:2px;width:5px;height:5px;background:var(--white)}

.product{position:absolute;width:208px;height:208px;overflow:hidden}
.product-photo{position:absolute;inset:0;background:radial-gradient(circle at 50% 45%,#a0663c 0,#7a4a2a 18%,#8a8a88 32%,#6e6e6c 60%,#2b2b2b 100%)}
.product-photo::after{content:"";position:absolute;inset:0;background:linear-gradient(to bottom,rgba(0,0,0,0) 45%,rgba(0,0,0,.55) 100%)}
.sale{position:absolute;left:10px;top:10px;background:var(--gold);color:var(--white);font-family:'Raleway',sans-serif;font-size:13px;padding:1px 5px;line-height:18px}
.product-name{position:absolute;left:10px;top:150px;font-family:'Open Sans',sans-serif;font-weight:600;font-size:11px;letter-spacing:1.5px}
.product-price{position:absolute;left:10px;top:170px;font-family:'Open Sans',sans-serif;font-weight:700;font-size:13px;letter-spacing:2px}

.pager{position:absolute;left:462px;top:962px;display:flex;align-items:center;gap:8px;font-family:'Open Sans',sans-serif;font-size:15px}
.page-current{width:26px;height:24px;border:1.5px solid var(--gold);text-align:center;line-height:21px}

.site-footer{position:absolute;left:0;top:1026px;width:1052px;height:174px;background:var(--footer)}
.footer-title{position:absolute;top:40px;font-size:12.5px;letter-spacing:2px;color:var(--gold)}
.footer-links{position:absolute;top:73px;list-style:none;font-family:'Raleway',sans-serif;font-size:13.5px;line-height:23px;color:var(--white)}
.footer-links a{color:var(--white);text-decoration:none}
.news-input{position:absolute;left:678px;top:75px;width:246px;height:45px;border-bottom:1px solid var(--grey);font-family:'Raleway',sans-serif;font-style:italic;font-size:13px;letter-spacing:1.5px;color:#4a4a4a;padding:20px 0 0 4px}
.news-btn{position:absolute;left:924px;top:75px;width:46px;height:45px;background:#3a3a3a}
.news-btn svg{position:absolute;left:17px;top:14px}
</style>
</head>
<body>

<header class="site-header">
  <a class="nav-link" style="left:171px" href="#">SHOP</a>
  <a class="nav-link" style="left:330px" href="#">ABOUT</a>
  <div class="brand"><span class="brand-mark"></span>Tidal Bloomz</div>
  <a class="nav-link" style="left:709px" href="#">PORTFOLIO</a>
  <a class="nav-link" style="left:873px" href="#">CONTACT</a>
</header>

<div class="filter-bar">
  <div class="crumbs">HOME / SHOP</div>
  <div class="chip" style="left:227px">Ring&nbsp;&nbsp;X</div>
  <div class="chip" style="left:297px">Gold&nbsp;&nbsp;X</div>
  <div class="sort-label">SORT BY:</div>
  <div class="sort-select">Popular
    <svg width="9" height="6" viewBox="0 0 9 6"><path d="M1 1l3.5 3.5L8 1" fill="none" stroke="#fff" stroke-width="1.3"/></svg>
  </div>
</div>

<aside class="filters">
  <h2>FILTERS</h2>
  <div class="filter-row" style="top:55px"><span class="toggle closed"></span>Category</div>
  <div class="filter-row" style="top:83px"><span class="toggle closed"></span>Material</div>
  <div class="filter-row" style="top:111px"><span class="toggle closed"></span>Price</div>
  <div class="filter-row" style="top:137px"><span class="toggle"></span>Size</div>
  <div class="size-opt" style="top:158px"><span class="box on"></span>U</div>
  <div class="size-opt" style="top:178px"><span class="box"></span>V</div>
  <div class="size-opt" style="top:198px"><span class="box"></span>W</div>
  <div class="size-opt" style="top:218px"><span class="box"></span>X</div>
  <div class="size-opt" style="top:237px"><span class="box"></span>Y</div>
  <div class="size-opt" style="top:257px"><span class="box"></span>Z</div>
  <div class="filter-row" style="top:286px"><span class="toggle closed"></span>Availability</div>
</aside>

<main>
  <article class="product" style="left:227px;top:207px"><div class="product-photo" role="img" aria-label="Gold sovereign coin ring on grey stone"></div><span class="sale">on sale</span><div class="product-name">GOLD FULL SOVEREIGN COIN</div><div class="product-price">$2400</div></article>
  <article class="product" style="left:488px;top:207px"><div class="product-photo" role="img" aria-label="Gold sovereign coin ring on grey stone"></div><div class="product-name">GOLD FULL SOVEREIGN COIN</div><div class="product-price">$2400</div></article>
  <article class="product" style="left:762px;top:207px"><div class="product-photo" role="img" aria-label="Gold sovereign coin ring on grey stone"></div><div class="product-name">GOLD FULL SOVEREIGN COIN</div><div class="product-price">$2400</div></article>

  <article class="product" style="left:227px;top:458px"><div class="product-photo" role="img" aria-label="Gold sovereign coin ring on grey stone"></div><span class="sale">on sale</span><div class="product-name">GOLD FULL SOVEREIGN COIN</div><div class="product-price">$2400</div></article>
  <article class="product" style="left:488px;top:458px"><div class="product-photo" role="img" aria-label="Gold sovereign coin ring on grey stone"></div><div class="product-name">GOLD FULL SOVEREIGN COIN</div><div class="product-price">$2400</div></article>
  <article class="product" style="left:762px;top:458px"><div class="product-photo" role="img" aria-label="Gold sovereign coin ring on grey stone"></div><div class="product-name">GOLD FULL SOVEREIGN COIN</div><div class="product-price">$2400</div></article>

  <article class="product" style="left:227px;top:717px"><div class="product-photo" role="img" aria-label="Gold sovereign coin ring on grey stone"></div><span class="sale">on sale</span><div class="product-name">GOLD FULL SOVEREIGN COIN</div><div class="product-price">$2400</div></article>
  <article class="product" style="left:488px;top:717px"><div class="product-photo" role="img" aria-label="Gold sovereign coin ring on grey stone"></div><div class="product-name">GOLD FULL SOVEREIGN COIN</div><div class="product-price">$2400</div></article>
  <article class="product" style="left:762px;top:717px"><div class="product-photo" role="img" aria-label="Gold sovereign coin ring on grey stone"></div><div class="product-name">GOLD FULL SOVEREIGN COIN</div><div class="product-price">$2400</div></article>

  <nav class="pager">
    <svg width="12" height="20" viewBox="0 0 12 20"><path d="M10 2L2 10l8 8" fill="none" stroke="#6b5a1e" stroke-width="1.5"/></svg>
    <span class="page-current">1</span>
    <span>2</span><span>...</span><span>5</span>
    <svg width="12" height="20" viewBox="0 0 12 20"><path d="M2 2l8 8-8 8" fill="none" stroke="#ffc214" stroke-width="1.5"/></svg>
  </nav>
</main>

<footer class="site-footer">
  <div class="footer-title" style="left:145px">FOLLOW US</div>
  <ul class="footer-links" style="left:146px">
    <li><a href="#">friendlio</a></li>
    <li><a href="#">picorama</a></li>
    <li><a href="#">swapzo</a></li>
  </ul>
  <div class="footer-title" style="left:350px">CONTACT US</div>
  <ul class="footer-links" style="left:350px"><li>+ 021 07351942</li></ul>
  <div class="footer-title" style="left:677px">SUBSCRIBE OUR NEWSLETTER</div>
  <div class="news-input">Enter your e-mail</div>
  <div class="news-btn"><svg width="12" height="18" viewBox="0 0 12 18"><path d="M2 1l8 8-8 8" fill="none" stroke="#9a9a9a" stroke-width="1.3"/></svg></div>
</footer>

</body>
</html>
```